Sam Greenfield Billboard

**Task Description: Billboard Design for Self Storage Facility**

**Objective:**
Design a captivating billboard to promote our self-storage facility with a focus on our convenient location and online rental capabilities.

**Key Messages to Include:**
1. **Location Emphasis:** Highlight that our facility is located right beside the billboard (maybe by using an arrow pointing left).
2. **Online Rental Convenience:** Feature prominently that customers can "Rent Online Anytime!” or that we are "Always Open Online!"

**Target Audience:**
- Local residents looking for convenient self-storage solutions.
- Businesses needing storage space accessible around the clock.

**Design Elements:**
1. **Visual Impact:** Eye-catching graphics and colors that stand out against the surroundings.
2. **Clear Text:** Bold and concise messaging that can be read and understood quickly.
3. **Contact Information:** Include our phone number and website URL for easy access to further information.

**Additional Information:**
- Billboard dimensions: 12 ft. x 24 ft.
- Preferred color scheme: Bright and attention-grabbing, but professional.
- Branding: Incorporate our logo and brand colors to maintain consistency.

**Deliverables:**
- High-resolution digital file compatible with billboard printing specifications.
- Consider mockups or visualizations for presentation purposes.

Please note that I have attached current logos/graphics that we would love to incorporate into the billboard as well as a picture of our current billboard. Our logo (Sam Greenfield Self Storage - SG navy.png) MUST be incorporated into the billboard. Also feel free to add any of the current descriptions from the picture of our current billboard into the design. Instead of using "Climate Controlled" use "Temperature Controlled". Thank you for your attention to these details. We look forward to reviewing your proposed design!

```html
<!DOCTYPE html>
<html lang="en">
<head>
<meta charset="utf-8">
<title>Sam Greenfield Billboard</title>
<link href="https://fonts.googleapis.com/css2?family=Montserrat:wght@600;800;900&family=Paytone+One&family=Oswald:wght@700&display=swap" rel="stylesheet">
<style>
  :root {
    --page-bg: #4a4a4c;
    --board-red: #b5121b;
    --frame-white: #ffffff;
    --navy: #1d2b5c;
    --ink: #151515;
    --green: #5cb335;
    --green-dark: #3f8f1f;
    --badge-red: #d0101c;
    --icon-grey: #4b4b4b;
  }
  * { margin: 0; padding: 0; box-sizing: border-box; }
  html, body { width: 1200px; height: 1200px; overflow: hidden; background: var(--page-bg); }
  .stage { position: relative; width: 1200px; height: 1200px; }
  .billboard {
    position: absolute; left: 40px; top: 320px;
    width: 1400px; height: 700px;
    transform: scale(0.8); transform-origin: 0 0;
    background: var(--board-red);
    box-shadow: 0 10px 30px rgba(0,0,0,.35);
  }
  .billboard-art { position: absolute; inset: 0; width: 1400px; height: 700px; }
  .brand {
    position: absolute; left: 0; right: 0; top: 62px; text-align: center;
    font-family: "Montserrat", sans-serif; color: var(--navy);
  }
  .brand-name { font-weight: 800; font-size: 44px; letter-spacing: 1px; line-height: 1; }
  .brand-tag { font-weight: 800; font-size: 19px; letter-spacing: 10px; margin-top: 8px; }
  .headline {
    position: absolute; left: 0; right: 0; top: 158px; text-align: center;
    font-family: "Montserrat", sans-serif; font-weight: 900; color: var(--navy);
    font-size: 84px; line-height: 80px; padding-left: 100px;
    text-shadow: 0 0 6px rgba(255,255,255,.9);
  }
  .features {
    position: absolute; left: 160px; right: 20px; top: 332px;
    display: flex; justify-content: center; gap: 30px; list-style: none;
    font-family: "Paytone One", sans-serif; font-size: 24px; color: var(--ink);
  }
  .feature { display: flex; align-items: center; gap: 8px; white-space: nowrap; }
  .feature svg { width: 28px; height: 28px; }
  .contact-line {
    position: absolute; left: 0; right: 0; top: 372px; text-align: center;
    font-family: "Paytone One", sans-serif; font-size: 24px; color: var(--ink);
    padding-left: 100px; word-spacing: 2px;
  }
  .contact-line .divider { margin: 0 26px; }
  .photo-strip {
    position: absolute; left: 370px; top: 437px; width: 755px; height: 150px;
    display: flex; gap: 3px;
  }
  .photo { flex: 1; height: 100%; }
  .photo-row-outdoor { background: linear-gradient(180deg, #a9c8e0 0%, #7d9a6a 40%, #4c5a45 60%, #3f4145 100%); }
  .photo-door-aisle { background: linear-gradient(90deg, #2f5040 0%, #3d6350 45%, #c9b894 60%, #3a3d42 100%); }
  .photo-hallway { background: linear-gradient(90deg, #27463a 0%, #c7b99e 45%, #d8cdb8 55%, #27463a 100%); }
  .photo-lock { background: radial-gradient(circle at 60% 50%, #d9d9d9 0%, #8a8a8a 35%, #3b3b3b 80%); }
  .web-pill {
    position: absolute; left: 540px; top: 600px; height: 52px;
    display: flex; align-items: center;
  }
  .web-icon {
    width: 56px; height: 56px; border-radius: 50%; background: var(--icon-grey);
    display: flex; align-items: center; justify-content: center; position: relative; z-index: 1;
    box-shadow: 0 2px 4px rgba(0,0,0,.3);
  }
  .web-url {
    margin-left: -10px; height: 46px; padding: 0 24px 0 28px;
    background: linear-gradient(180deg, #7fd04f, var(--green-dark));
    border-radius: 0 23px 23px 0;
    display: flex; align-items: center;
    font-family: "Montserrat", sans-serif; font-weight: 600; font-size: 21px; color: var(--ink);
  }
  .online-badge {
    position: absolute; left: 1212px; top: 22px; width: 180px; height: 150px;
  }
  .online-badge svg { position: absolute; left: 0; top: 0; }
  .badge-text {
    position: absolute; inset: 0;
    font-family: "Oswald", sans-serif; font-weight: 700; font-style: italic;
    color: var(--frame-white); line-height: 1;
  }
  .badge-always { position: absolute; right: 20px; top: 14px; font-size: 18px; letter-spacing: 1px; }
  .badge-open { position: absolute; left: 28px; top: 32px; font-size: 56px; letter-spacing: 1px; }
  .badge-online { position: absolute; left: 28px; top: 92px; font-size: 17px; }
</style>
</head>
<body>
<main class="stage">
  <section class="billboard" aria-label="Sam Greenfield Self Storage billboard">
    <svg class="billboard-art" viewBox="0 0 1400 700" xmlns="http://www.w3.org/2000/svg">
      <defs>
        <linearGradient id="aerialTone" x1="0" y1="0" x2="1" y2="1">
          <stop offset="0" stop-color="#ecebe8"/>
          <stop offset="0.45" stop-color="#d8d6d1"/>
          <stop offset="0.75" stop-color="#cfcbc2"/>
          <stop offset="1" stop-color="#e2dfda"/>
        </linearGradient>
        <linearGradient id="curlTone" x1="0" y1="0" x2="1" y2="1">
          <stop offset="0" stop-color="#ffffff"/>
          <stop offset="0.6" stop-color="#e9e9e9"/>
          <stop offset="1" stop-color="#bdbdbd"/>
        </linearGradient>
      </defs>
      <path class="panel-frame" d="M262 20 L1068 20 Q1250 150 1385 262 L1385 680 L240 680 L52 347 Z" fill="var(--frame-white)"/>
      <path class="panel-aerial" role="img" aria-label="Aerial view of the storage facility with rows of unit buildings and a road"
            d="M270 34 L1060 34 Q1230 160 1372 270 L1372 666 L248 666 L68 347 Z" fill="url(#aerialTone)"/>
      <path class="page-curl" d="M1060 34 Q1180 60 1260 140 Q1320 200 1372 270 Q1290 240 1230 170 Q1150 90 1060 34 Z" fill="url(#curlTone)"/>
      <path d="M1060 34 Q1200 130 1372 270" fill="none" stroke="#cfcfcf" stroke-width="2"/>
    </svg>

    <div class="brand">
      <div class="brand-name">SAM GREENFIELD</div>
      <div class="brand-tag">SELF STORAGE</div>
    </div>

    <h1 class="headline">SELF STORAGE<br>SERVICES</h1>

    <ul class="features">
      <li class="feature"><svg viewBox="0 0 28 28"><circle cx="14" cy="14" r="11" fill="none" stroke="var(--green)" stroke-width="3"/><path d="M8 14 L13 19 L24 6" fill="none" stroke="var(--green)" stroke-width="3.5" stroke-linecap="round"/></svg>LARGE / SMALL UNITS</li>
      <li class="feature"><svg viewBox="0 0 28 28"><circle cx="14" cy="14" r="11" fill="none" stroke="var(--green)" stroke-width="3"/><path d="M8 14 L13 19 L24 6" fill="none" stroke="var(--green)" stroke-width="3.5" stroke-linecap="round"/></svg>TEMPERATURE CONTROLLED</li>
      <li class="feature"><svg viewBox="0 0 28 28"><circle cx="14" cy="14" r="11" fill="none" stroke="var(--green)" stroke-width="3"/><path d="M8 14 L13 19 L24 6" fill="none" stroke="var(--green)" stroke-width="3.5" stroke-linecap="round"/></svg>COVERED BOAT / RV PARKING</li>
    </ul>

    <p class="contact-line">215 MAPLE RIDGE DRIVE<span class="divider">|</span>478-555-0142</p>

    <div class="photo-strip">
      <div class="photo photo-row-outdoor" role="img" aria-label="Outdoor row of storage units under a blue sky"></div>
      <div class="photo photo-door-aisle" role="img" aria-label="Green roll-up storage doors along a paved aisle"></div>
      <div class="photo photo-hallway" role="img" aria-label="Indoor temperature controlled hallway of units"></div>
      <div class="photo photo-lock" role="img" aria-label="Close-up of a disc lock on a unit door"></div>
    </div>

    <div class="web-pill">
      <div class="web-icon">
        <svg width="34" height="34" viewBox="0 0 34 34" fill="none" stroke="#fff" stroke-width="2.4">
          <circle cx="16" cy="16" r="12"/><ellipse cx="16" cy="16" rx="5" ry="12"/><path d="M4 16 H28 M6 10 H26 M6 22 H26"/>
          <path d="M22 22 L31 26 L27 27 L26 31 Z" fill="#fff" stroke="none"/>
        </svg>
      </div>
      <div class="web-url">WWW.OAKRIDGESTORAGEGROUP.COM</div>
    </div>

    <div class="online-badge">
      <svg width="180" height="150" viewBox="0 0 180 150">
        <path d="M10 12 L174 6 L168 118 L118 120 L104 148 L98 121 L16 124 Z" fill="var(--badge-red)" stroke="var(--green)" stroke-width="7" stroke-linejoin="miter"/>
      </svg>
      <div class="badge-text">
        <span class="badge-always">ALWAYS</span>
        <span class="badge-open">OPEN</span>
        <span class="badge-online">ONLINE!</span>
      </div>
    </div>
  </section>
</main>
</body>
</html>
```